Modern Lawfirm Business Card Design

We're looking for a business card to incorporate the newly created logo we had made.

Ideally looking for a law firm business card demonstrating, modern, minimalist, strong/bold design.

I'm open to any design honestly, but nothing "flashy".

Target Market(s)

Immigration law, family immigration, humanitarian, general legal

Industry/Entity Type

Law Firm

Contact Information for Business Card

Please use dummy information, name, street address, city, state, phone number, email, website.

Font styles to use
Serif
Sans Serif

Requirements
Must have
• Please use dummy information, name, street address, city, state, phone number, email, website.

```html
<!DOCTYPE html>
<html lang="en">
<head>
<meta charset="utf-8">
<title>Marlowe Immigration Law – Business Card</title>
<link href="https://fonts.googleapis.com/css2?family=Open+Sans:wght@400;600;700&display=swap" rel="stylesheet">
<style>
  :root {
    --backdrop: #c9cacc;
    --ink: #222222;
    --paper: #e4e4e4;
    --white: #ffffff;
    --rule-light: #d8d8d8;
  }
  html, body {
    margin: 0;
    padding: 0;
    width: 1200px;
    height: 1200px;
    overflow: hidden;
    background: var(--backdrop);
  }
  .canvas {
    display: block;
    width: 1200px;
    height: 1200px;
    font-family: "Open Sans", Arial, sans-serif;
  }
  .fill-ink { fill: var(--ink); }
  .fill-paper { fill: var(--paper); }
  .fill-white { fill: var(--white); }
  .rule-dark { stroke: var(--ink); stroke-width: 3; }
  .rule-light { stroke: var(--rule-light); stroke-width: 3; }
  .name { font-size: 31px; font-weight: 700; letter-spacing: 1px; }
  .name--first { fill: var(--paper); }
  .name--last { fill: var(--ink); }
  .position { font-size: 15px; font-weight: 600; fill: var(--paper); }
  .contact { font-size: 14px; font-weight: 700; fill: var(--ink); letter-spacing: 0.3px; }
  .icon { fill: var(--white); }
  .icon-stroke { fill: none; stroke: var(--white); stroke-width: 2.4; stroke-linecap: round; }
  .firm-name { font-size: 24px; font-weight: 700; fill: var(--white); letter-spacing: 1px; }
</style>
</head>
<body>
<svg class="canvas" viewBox="0 0 1200 1200" xmlns="http://www.w3.org/2000/svg">

  <!-- Front of card -->
  <g class="card card--front">
    <rect class="fill-paper" x="212" y="113" width="777" height="430"/>
    <polygon class="fill-ink" points="212,113 543,113 657,543 212,543"/>

    <line class="rule-dark" x1="573" y1="232" x2="848" y2="157"/>
    <line class="rule-light" x1="322" y1="383" x2="595" y2="313"/>

    <g transform="rotate(-15.3)">
      <g transform="translate(0 0)"></g>
    </g>

    <text class="name name--first" transform="translate(464 252) rotate(-15.3)">JOHN</text>
    <text class="name name--last" transform="translate(584 208) rotate(-15.3)">DOE</text>
    <text class="position" transform="translate(453 284) rotate(-15.3)">title / position</text>

    <text class="contact" transform="translate(612 334) rotate(-15.3)">Main street, Your Loc,</text>
    <text class="contact" transform="translate(617 353) rotate(-15.3)">Number 12/A, 45678</text>
    <text class="contact" transform="translate(627 388) rotate(-15.3)">info@email.com</text>
    <text class="contact" transform="translate(641 429) rotate(-15.3)">+ 012 34 56 789</text>
    <text class="contact" transform="translate(653 474) rotate(-15.3)">www.company.com</text>

    <!-- pin -->
    <g transform="translate(573 350) rotate(-15.3)">
      <path class="icon" d="M0,12 C-7,3 -8,-1 -8,-3 A8,8 0 0 1 8,-3 C8,-1 7,3 0,12 Z M0,-6 A3,3 0 1 0 0.01,-6 Z" fill-rule="evenodd"/>
    </g>
    <!-- envelope -->
    <g transform="translate(587 397) rotate(-15.3)">
      <rect class="icon" x="-11" y="-8" width="22" height="16"/>
      <polyline points="-11,-8 0,2 11,-8" fill="none" stroke="#222222" stroke-width="1.6"/>
    </g>
    <!-- phone -->
    <g transform="translate(600 437) rotate(-15.3)">
      <path class="icon" d="M-8,-9 L-4,-10 L-1,-4 L-4,-2 C-3,2 0,5 3,6 L5,3 L10,6 L9,10 C2,11 -9,1 -8,-9 Z"/>
    </g>
    <!-- web / wifi -->
    <g transform="translate(609 485) rotate(-15.3)">
      <path class="icon-stroke" d="M-11,-3 A15,15 0 0 1 11,-3"/>
      <path class="icon-stroke" d="M-7,1 A9,9 0 0 1 7,1"/>
      <path class="icon-stroke" d="M-3,5 A4,4 0 0 1 3,5"/>
      <circle class="icon" cx="0" cy="8" r="1.8"/>
    </g>
  </g>

  <!-- Back of card -->
  <g class="card card--back">
    <rect class="fill-ink" x="212" y="656" width="777" height="430"/>
    <polygon class="fill-paper" points="212,656 478,656 511,772 212,856"/>
    <polygon class="fill-paper" points="690,967 989,890 989,1086 722,1086"/>

    <g class="firm-mark" transform="translate(580 880) rotate(-15.3)">
      <rect class="fill-white" x="-150" y="-14" width="14" height="14"/>
      <text class="firm-name" x="-126" y="0">MARLOWE IMMIGRATION LAW</text>
    </g>
  </g>
</svg>
</body>
</html>
```